A4 Flier to send to Schools about Manners for School Students

We are expanding and now working with corporate clients as well as teaching etiquette and manners to High School students. This is a the flier we need created. The clients are Assistant Principals and Heads of School so we need to appear professional, approachable and aspirational and fun.
Here is the content and some images that may be useful to get started.

Target Market(s)

Assistant Principals and School Heads

Industry/Entity Type

School

Font styles to use
Sans Serif

Colors
00a990
ffffff

Requirements
Must have
• Cool pictures of young people - pref a mix of Asians, caucasians. Well dressed and happy teens and positive images.
• Logo
• Some use of green and white as this is our corporate style.
• Image of Clara Pendry
• Image of Ingrid Dowlatte
Nice to have
• I have put it all in the flier I have attached so please come back to me with any questions.
Should not have
• Any teens of African descent - only as Australian is mostly caucasian and Asian.
• Pinks

```html
<!DOCTYPE html>
<html lang="en">
<head>
<meta charset="utf-8">
<title>Etiquette &amp; Manners for Students</title>
<link href="https://fonts.googleapis.com/css2?family=Oswald:wght@400;500;700&family=Open+Sans:wght@400;600;700&display=swap" rel="stylesheet">
<style>
:root{
  --green:#00a990;
  --ink:#1c2126;
  --panel:#262c32;
  --white:#ffffff;
  --muted:#d6dcdf;
  --rule:#4a535b;
}
*{margin:0;padding:0;box-sizing:border-box}
html,body{width:857px;height:1200px;overflow:hidden;background:var(--ink)}
.flier{position:relative;width:857px;height:1200px;background:var(--ink);font-family:"Open Sans",sans-serif;color:var(--white)}
.left-col{position:absolute;left:0;top:0;width:425px;height:1200px;background:var(--panel)}
.brand{position:absolute;left:70px;top:38px;display:flex;align-items:center;gap:12px}
.brand-dot{width:34px;height:34px;border-radius:50%;background:var(--green)}
.brand-name{font-family:"Oswald",sans-serif;font-weight:500;font-size:24px;line-height:1.05;color:var(--white)}
.presents{position:absolute;left:70px;top:112px;font-family:"Oswald",sans-serif;font-size:16px;letter-spacing:1px}
.title-band{position:absolute;left:0;top:142px;width:415px;height:160px;background:var(--white);padding:12px 0 0 52px}
.title-band h1{font-family:"Oswald",sans-serif;font-weight:700;font-size:40px;line-height:1.08;color:var(--ink);text-transform:uppercase}
.portraits{position:absolute;left:40px;top:318px;width:350px;height:220px}
.portrait{position:absolute;border-radius:50%;background:radial-gradient(circle at 50% 40%,#c9ced2,#6f7a82);border:5px solid var(--white)}
.portrait.one{left:0;top:20px;width:185px;height:185px}
.portrait.two{left:160px;top:0;width:185px;height:185px}
.agenda{position:absolute;left:20px;top:565px;width:385px;text-align:center;font-size:13px;line-height:1.6}
.agenda h2{font-family:"Oswald",sans-serif;font-weight:500;font-size:17px;color:var(--green);text-transform:uppercase;margin-bottom:8px}
.agenda h3{font-family:"Oswald",sans-serif;font-weight:500;font-size:16px;color:var(--white);margin:12px 0 4px;border-top:1px solid var(--rule);padding-top:8px}
.agenda p{color:var(--muted)}
.intro-heading{position:absolute;left:460px;top:60px;width:370px;font-family:"Oswald",sans-serif;font-weight:500;font-size:20px;line-height:1.3;text-transform:uppercase}
.intro-text{position:absolute;left:460px;top:165px;width:365px;font-size:13.5px;line-height:1.55;color:var(--muted)}
.topics{position:absolute;left:470px;top:405px;width:360px;font-size:13.5px;line-height:1.5}
.topics h2{font-family:"Oswald",sans-serif;font-weight:500;font-size:18px;color:var(--green);margin-bottom:4px}
.topics li{list-style:none}
.table-photo{position:absolute;left:575px;top:660px;width:282px;height:305px;background:linear-gradient(150deg,#e5e3dc,#8e9186 60%,#3d4240)}
.price{position:absolute;left:395px;top:710px;width:180px;height:180px;border-radius:50%;background:var(--green);border:5px solid var(--white);display:flex;flex-direction:column;align-items:center;justify-content:center;text-align:center;font-family:"Oswald",sans-serif;font-weight:700;font-size:18px;line-height:1.2;color:var(--white);text-transform:uppercase;z-index:2}
.included{position:absolute;left:460px;top:990px;width:370px;font-size:13.5px;line-height:1.6}
.included h2{font-family:"Oswald",sans-serif;font-weight:500;font-size:18px;color:var(--green);margin-bottom:4px;text-transform:uppercase}
.included li{list-style:none}
</style>
</head>
<body>
<main class="flier">
  <div class="left-col"></div>

  <div class="brand">
    <span class="brand-dot"></span>
    <span class="brand-name">The Fine Conduct<br>Company</span>
  </div>
  <p class="presents">PRESENTS SESSIONS ON</p>

  <div class="title-band">
    <h1>Etiquette &amp;<br>Manners for<br>Students</h1>
  </div>

  <div class="portraits">
    <div class="portrait one" role="img" aria-label="Portrait photo of Clara Pendry"></div>
    <div class="portrait two" role="img" aria-label="Portrait photo of Ingrid Dowlatte"></div>
  </div>

  <section class="agenda">
    <h2>Sample One Hour Agenda</h2>
    <h3>Introduction</h3>
    <p>• What are good vs bad manners?<br>• Why it is important today?</p>
    <h3>The Rules</h3>
    <p>• Appropriate conduct for young ladies and gentlemen.</p>
    <h3>The First Impression</h3>
    <p>• How to make a good first impression.<br>• Speaking clearly.<br>• What to wear, where and when, dressing appropriately for the occasion.<br>• What not to wear, where and when incl job interviews.</p>
    <h3>Introductions</h3>
    <p>• How to introduce yourself correctly.<br>• How to introduce one person to another.<br>• Handshaking skills.<br>• Putting it all together.<br>• Role plays.</p>
  </section>

  <h2 class="intro-heading">Are you frustrated by the lack of manners and courtesy shown by students today?</h2>
  <p class="intro-text">Reports show that students are applying for jobs lacking social skills and etiquette, making them unprepared for part time jobs and full time workplaces. The sooner they learn good habits around manners and etiquette, the more well-rounded and prepared they will be for leadership opportunities, employment and forming good relationships.</p>

  <section class="topics">
    <h2>TOPICS</h2>
    <ul>
      <li>• Modern manners for young people.</li>
      <li>• How to introduce and others yourself correctly.</li>
      <li>• Job Interview Preparation.</li>
      <li>• Formal Preparation.</li>
      <li>• Netiquette, conduct with mobiles, devices and social media.</li>
      <li>• Table Manners.</li>
      <li>• Deportment, how to walk, sit, carry yourself with poise and confidence.</li>
      <li>• Dating Etiquette.</li>
    </ul>
  </section>

  <div class="table-photo" role="img" aria-label="Photo of a formal table setting with plate and cutlery"></div>

  <div class="price">Prices from<br>$500 for 1 hour<br>to<br>$1500 for a day</div>

  <section class="included">
    <h2>What's Included</h2>
    <ul>
      <li>• Handout to take home to parents.</li>
      <li>• Classroom poster.</li>
      <li>• Copy of "Courtesy Keys" book for School.</li>
    </ul>
  </section>
</main>
</body>
</html>
```